TovaLamarpe - Israeli Mental Health Website

We are developing an Israeli website for mental health. The website will be both in English and in Hebrew. We have a logo and would like a website design based on the logo and the logos colors (attached).

Attached is a doc that contains the website requirements.

We would like to have an icon for each of the sidebar categories, an image for each of the pages (including each of the sidebar category pages).

Target Market(s)

Adults 18-80

Industry/Entity Type

Mental Health

Number of Pages Required

5+ page

Font styles to use
Sans Serif

Colors

Designer to choose colors to be used in the design.

```html
<!DOCTYPE html>
<html lang="en">
<head>
<meta charset="utf-8">
<title>TovaLamarpe – Mental Health</title>
<link href="https://fonts.googleapis.com/css2?family=Urbanist:wght@500;600&family=Poppins:wght@400;500&display=swap" rel="stylesheet">
<style>
:root{
  --blue:#1f6fbf;
  --blue-dark:#1a5fa8;
  --green:#4caf45;
  --green-soft:#f1f8ef;
  --blue-soft:#eaf2fb;
  --text:#4a4f55;
  --white:#ffffff;
}
*{margin:0;padding:0;box-sizing:border-box}
html,body{width:1200px;height:3748px;overflow:hidden;background:var(--white)}
body{position:relative;font-family:"Poppins",sans-serif;color:var(--text)}
.abs{position:absolute}
h1,h2{font-family:"Urbanist",sans-serif;font-weight:500}
.header{top:0;left:0;width:1200px;height:97px}
.wa-icon{left:60px;top:29px;width:38px;height:38px;border-radius:50%;background:var(--green)}
.wa-label{left:120px;top:29px;font-size:13px;font-weight:500;color:#222}
.wa-number{left:120px;top:52px;font-size:14px;font-weight:500;color:var(--blue);letter-spacing:1px}
.brand{left:500px;top:34px;width:200px;text-align:center;font-family:"Poppins",sans-serif;font-size:22px;font-weight:500;color:var(--blue)}
.lang{right:60px;top:42px;font-size:13px;display:flex;gap:16px}
.lang a{color:var(--blue);text-decoration:underline}
.lang span.sep{width:1px;height:20px;background:#bbb;margin-top:-2px}
.nav{top:97px;left:0;width:1200px;height:44px;background:var(--blue);display:flex;align-items:center;justify-content:space-around;padding:0 100px;font-size:13px;color:var(--white)}
.hero{top:141px;left:0;width:1200px;height:690px;overflow:hidden}
.hero-photo{width:100%;height:100%;background:linear-gradient(120deg,#9a8f80 0%,#bfb7ab 35%,#6f8aa0 60%,#c9c2b9 100%)}
.hero-curve{left:0;top:0}
.hero-box{left:60px;top:111px;width:449px;height:323px;background:rgba(92,178,80,.82);border-radius:12px;padding:38px 34px;color:var(--white)}
.hero-box h1{font-size:50px;line-height:56px;font-weight:500}
.hero-box p{font-size:13px;line-height:22px;margin-top:16px}
.btn{display:inline-flex;align-items:center;height:36px;border-radius:18px;background:var(--blue);color:var(--white);font-size:13px;padding-left:20px;padding-right:4px;gap:14px}
.btn i{width:30px;height:30px;border-radius:50%;background:var(--white);border:2px solid var(--green)}
.hero-box .btn{margin-top:22px}
.sec-title{font-size:38px;color:var(--blue)}
.sec-title em{font-style:normal;color:var(--green)}
.sec-text{font-size:13px;line-height:22px;color:var(--text)}
.emerg-text{left:60px;top:980px;width:520px}
.emerg-text .sec-text{margin:16px 0 34px}
.emerg-panel{left:690px;top:899px;width:450px;height:436px;background:var(--green-soft);border-radius:18px}
.arrow{left:218px;width:0;height:0;border-left:9px solid transparent;border-right:9px solid transparent}
.arrow.up{top:24px;border-bottom:9px solid var(--green)}
.arrow.down{bottom:24px;border-top:9px solid #111}
.cats{left:54px;top:55px;width:342px;list-style:none}
.cats li{height:44px;margin-bottom:14px;border-radius:22px;background:var(--blue);color:var(--white);font-size:13px;display:flex;align-items:center;gap:16px;padding-left:3px}
.cats li.active{background:var(--green)}
.cats li i{width:38px;height:38px;border-radius:50%;background:var(--white);display:flex;align-items:center;justify-content:center}
.cats li i b{width:14px;height:14px;border-radius:50%;background:var(--blue)}
.cats li.active i b{background:var(--green)}
.band{height:466px}
.band.left{left:0;width:1200px;background:linear-gradient(90deg,var(--blue-soft),#f5f9fd);border-radius:0 240px 240px 0}
.band.right{left:330px;width:870px;background:linear-gradient(90deg,#f7fbf5,var(--green-soft));border-radius:240px 0 0 240px}
.photo{width:426px;height:426px;border-radius:50%;border:6px solid var(--blue)}
.photo.g{border-color:var(--green)}
.block{width:500px}
.block .sec-text{margin:16px 0 34px}
.play{left:187px;top:187px;width:52px;height:52px;border-radius:50%;background:var(--green);display:flex;align-items:center;justify-content:center}
.play span{width:0;height:0;border-top:9px solid transparent;border-bottom:9px solid transparent;border-left:13px solid var(--white);margin-left:4px}
.footer{left:0;top:3607px;width:1200px;height:141px;background:var(--blue);color:var(--white)}
.foot-nav{left:60px;top:44px;display:flex;gap:56px;font-size:13px}
.socials{right:60px;top:38px;display:flex;gap:14px}
.socials span{width:26px;height:26px;border-radius:50%;background:var(--white)}
.socials span:first-child{background:var(--green)}
.foot-line{left:0;top:98px;width:1200px;height:1px;background:rgba(255,255,255,.35)}
.copy{left:60px;top:112px;font-size:11px}
.legal{right:60px;top:112px;font-size:11px;display:flex;gap:30px}
</style>
</head>
<body>
<header class="header abs">
  <div class="wa-icon abs"></div>
  <div class="wa-label abs">Chat Line On</div>
  <div class="wa-number abs">05X-XXXXXXX</div>
  <div class="brand abs">TovaLamarpe</div>
  <div class="lang abs"><span>עברית</span><span class="sep"></span><a>English</a></div>
</header>
<nav class="nav abs">
  <span>Smart ChatLine</span><span>Therapists</span><span>Organizations</span><span>Videos</span><span>About</span><span>Contact</span><span>Donate</span>
</nav>

<section class="hero abs">
  <div class="hero-photo" role="img" aria-label="Two young women talking on outdoor stone steps"></div>
  <svg class="hero-curve abs" width="1200" height="690" viewBox="0 0 1200 690">
    <path d="M0 480 Q560 860 1200 420 L1200 690 L0 690 Z" fill="#ffffff"/>
    <path d="M0 480 Q560 860 1200 420" fill="none" stroke="#1f6fbf" stroke-width="16"/>
    <path d="M40 460 Q580 810 1200 420" fill="none" stroke="#4caf45" stroke-width="8"/>
  </svg>
  <div class="hero-box abs">
    <h1>Talk. Resolve. Be Happier.</h1>
    <p>Lorem ipsum dolor sit amet, consectetur adipiscing elit, sed do eiusmod tempor incididunt ut labore et dolore magna aliqua.</p>
    <span class="btn">Contact Us Today <i></i></span>
  </div>
</section>

<section class="emerg-text abs">
  <h2 class="sec-title">Emergency <em>Mental Help</em></h2>
  <p class="sec-text">Lorem ipsum dolor sit amet, consectetur adipiscing elit, sed do eiusmod tempor incididunt ut labore et dolore magna aliqua. Ut enim ad minim veniam, quis nostrud exercitation ullamco laboris nisi ut aliquip ex ea commodo consequat. Duis aute irure dolor in reprehenderit in voluptate velit esse cillum dolore eu fugiat nulla pariatur. Excepteur sint occaecat cupidatat non proident, sunt in culpa qui officia deserunt mollit anim id est laborum.</p>
  <span class="btn">More options for Emergency Mental Help <i></i></span>
</section>
<aside class="emerg-panel abs">
  <span class="arrow up abs"></span>
  <ul class="cats abs">
    <li class="active"><i><b></b></i>Emergency Mental Help</li>
    <li><i><b></b></i>Suicide</li>
    <li><i><b></b></i>Sexual Assault/Violence Victims</li>
    <li><i><b></b></i>Sexual Assault/Violence Assaulters</li>
    <li><i><b></b></i>Post Trauma</li>
    <li><i><b></b></i>Depression</li>
  </ul>
  <span class="arrow down abs"></span>
</aside>

<section class="band left abs" style="top:1450px"></section>
<div class="block abs" style="left:60px;top:1555px">
  <h2 class="sec-title">Smart <em>ChatLine</em></h2>
  <p class="sec-text">Lorem ipsum dolor sit amet, consectetur adipiscing elit, sed do eiusmod tempor incididunt ut labore et dolore magna aliqua. Ut enim ad minim veniam, quis nostrud exercitation ullamco laboris nisi ut aliquip ex ea commodo consequat. Duis aute irure dolor in reprehenderit in voluptate velit esse cillum dolore eu fugiat nulla pariatur. Excepteur sint occaecat cupidatat non proident, sunt in culpa qui officia deserunt mollit anim id est laborum.</p>
  <span class="btn" style="letter-spacing:1px">05X-XXXXXXX <i></i></span>
</div>
<div class="photo abs" style="left:674px;top:1470px;background:radial-gradient(circle at 55% 45%,#e8e8e8,#5a5a5a 60%,#2e2e2e)" role="img" aria-label="Hands holding a smartphone with a chat app open"></div>

<section class="band right abs" style="top:1985px"></section>
<div class="photo g abs" style="left:98px;top:2005px;background:linear-gradient(160deg,#e9e4dc,#cbb8a2 50%,#a9b9c8)" role="img" aria-label="Smiling therapist seated with a tablet"></div>
<div class="block abs" style="left:589px;top:2070px">
  <h2 class="sec-title" style="line-height:46px">Professional, licensed, and <em>vetted therapists</em></h2>
  <p class="sec-text">Lorem ipsum dolor sit amet, consectetur adipiscing elit, sed do eiusmod tempor incididunt ut labore et dolore magna aliqua. Ut enim ad minim veniam, quis nostrud exercitation ullamco laboris nisi ut aliquip ex ea commodo consequat. Duis aute irure dolor in reprehenderit in voluptate velit esse cillum dolore eu fugiat nulla pariatur. Excepteur sint occaecat cupidatat non proident, sunt in culpa qui officia deserunt mollit anim id est laborum.</p>
  <span class="btn">Find Therapists <i></i></span>
</div>

<section class="band left abs" style="top:2527px"></section>
<div class="block abs" style="left:60px;top:2630px">
  <h2 class="sec-title">Organizations</h2>
  <p class="sec-text">Lorem ipsum dolor sit amet, consectetur adipiscing elit, sed do eiusmod tempor incididunt ut labore et dolore magna aliqua. Ut enim ad minim veniam, quis nostrud exercitation ullamco laboris nisi ut aliquip ex ea commodo consequat. Duis aute irure dolor in reprehenderit in voluptate velit esse cillum dolore eu fugiat nulla pariatur. Excepteur sint occaecat cupidatat non proident, sunt in culpa qui officia deserunt mollit anim id est laborum.</p>
  <span class="btn">Find Organizations <i></i></span>
</div>
<div class="photo abs" style="left:674px;top:2543px;background:radial-gradient(circle at 50% 50%,#d9a98a,#8a5a44 60%,#3e4a5a)" role="img" aria-label="Stacked hands showing support"></div>

<section class="band right abs" style="top:3059px"></section>
<div class="photo g abs" style="left:98px;top:3077px;background:linear-gradient(160deg,#cfd6dc,#8fa0ad 50%,#e4e0da)" role="img" aria-label="Woman meditating in a bright room">
  <div class="play abs"><span></span></div>
</div>
<div class="block abs" style="left:589px;top:3160px">
  <h2 class="sec-title">Videos</h2>
  <p class="sec-text">Lorem ipsum dolor sit amet, consectetur adipiscing elit, sed do eiusmod tempor incididunt ut labore et dolore magna aliqua. Ut enim ad minim veniam, quis nostrud exercitation ullamco laboris nisi ut aliquip ex ea commodo consequat. Duis aute irure dolor in reprehenderit in voluptate velit esse cillum dolore eu fugiat nulla pariatur. Excepteur sint occaecat cupidatat non proident, sunt in culpa qui officia deserunt mollit anim id est laborum.</p>
  <span class="btn">Video Library <i></i></span>
</div>

<footer class="footer abs">
  <div class="foot-nav abs"><span>Smart ChatLine</span><span>Therapists</span><span>Organizations</span><span>Videos</span><span>About</span><span>Contact</span><span>Donate</span></div>
  <div class="socials abs"><span></span><span></span><span></span><span></span></div>
  <div class="foot-line abs"></div>
  <div class="copy abs">TovaLamarpe - Organization for Mental Health ©2023</div>
  <div class="legal abs"><span>Privacy Policy</span><span>Terms</span></div>
</footer>
</body>
</html>
```